Small office needs Graphic works to walls

Based on the company's logo and branding, create graphic illustrations that could be applied to the walls to enhance the interiors. The company's line of work is project management.
Their corporate brand guidelines can be downloaded from this link https://www.vellumcrate.net/sh/qkmtvbznp4lx8/AAHrtyKLwqZ7nT-p93M2-Kxbn?dl=0
Photos of the existing space (along with a Key Plan) have been uploaded.

Target Market(s)

The target is to offer clients that are visiting the office a glimpse of the company's identity and what they do

Font styles to use
Other font styles liked:
• MinionPro-Regular and Futura

Requirements
Must have
• The graphics should relate to the corporate identiy
Nice to have
• keep it simple but effective

```html
<!DOCTYPE html>
<html lang="en">
<head>
<meta charset="utf-8">
<title>Office Wall Graphics – Word Clouds</title>
<link rel="stylesheet" href="https://fonts.googleapis.com/css2?family=Jost:wght@400;500&display=swap">
<style>
  :root {
    --wall: #ffffff;
    --ink-navy: #1d5a88;
    --ink-mid: #2577b6;
    --ink-sky: #2c9ad7;
  }
  html, body {
    margin: 0;
    padding: 0;
    width: 1200px;
    height: 590px;
    overflow: hidden;
    background: var(--wall);
  }
  .wall-graphics {
    display: block;
    width: 1200px;
    height: 528px;
    margin-top: 31px;
  }
  .wall-graphics text {
    font-family: "Jost", "Futura", sans-serif;
    font-weight: 400;
  }
  .navy { fill: var(--ink-navy); }
  .mid { fill: var(--ink-mid); }
  .sky { fill: var(--ink-sky); }
</style>
</head>
<body>
<svg class="wall-graphics" viewBox="375 385 750 330" role="img" aria-label="Two word-cloud wall graphics: company values and sector expertise">
  <g class="cloud cloud-values">
    <text class="sky" x="406" y="698" font-size="22" textLength="306" lengthAdjust="spacingAndGlyphs" transform="rotate(-90 406 698)">Collaboration &amp; Teamwork</text>
    <text class="navy" x="415" y="417" font-size="24" textLength="140" lengthAdjust="spacingAndGlyphs">Leadership</text>
    <text class="sky" x="422" y="470" font-size="11" textLength="50" lengthAdjust="spacingAndGlyphs" transform="rotate(-90 422 470)">Delivery</text>
    <text class="navy" x="435" y="445" font-size="22" textLength="100" lengthAdjust="spacingAndGlyphs">Expertise</text>
    <text class="navy" x="435" y="471" font-size="19" textLength="100" lengthAdjust="spacingAndGlyphs">Experience</text>
    <text class="sky" x="542" y="425" font-size="11" textLength="50" lengthAdjust="spacingAndGlyphs" transform="rotate(90 542 425)">Execution</text>
    <text class="sky" x="564" y="395" font-size="12" textLength="80" lengthAdjust="spacingAndGlyphs" transform="rotate(90 564 395)">IT Integration</text>
    <text class="navy" x="582" y="422" font-size="36" textLength="135" lengthAdjust="spacingAndGlyphs">People</text>
    <text class="mid" x="582" y="467" font-size="36" textLength="130" lengthAdjust="spacingAndGlyphs">Quality</text>
    <text class="navy" x="417" y="507" font-size="32" textLength="290" lengthAdjust="spacingAndGlyphs">Customer Service</text>
    <text class="sky" x="417" y="610" font-size="11" textLength="95" lengthAdjust="spacingAndGlyphs" transform="rotate(-90 417 610)">Bespoke IT Solutions</text>
    <text class="mid" x="433" y="558" font-size="56" textLength="227" lengthAdjust="spacingAndGlyphs">Business</text>
    <text class="mid" x="433" y="603" font-size="56" textLength="227" lengthAdjust="spacingAndGlyphs">Priorities</text>
    <text class="navy" x="667" y="517" font-size="16" textLength="95" lengthAdjust="spacingAndGlyphs" transform="rotate(90 667 517)">Ownership</text>
    <text class="navy" x="694" y="517" font-size="16" textLength="148" lengthAdjust="spacingAndGlyphs" transform="rotate(90 694 517)">Vision Alignment</text>
    <text class="sky" x="432" y="640" font-size="26" textLength="245" lengthAdjust="spacingAndGlyphs">Active Engagement</text>
    <text class="navy" x="415" y="663" font-size="14" textLength="262" lengthAdjust="spacingAndGlyphs">Building Information Modelling (BIM)</text>
    <text class="navy" x="415" y="697" font-size="32" textLength="297" lengthAdjust="spacingAndGlyphs">Forward Technology</text>
  </g>
  <g class="cloud cloud-sectors">
    <text class="navy" x="778" y="430" font-size="40" textLength="339" lengthAdjust="spacingAndGlyphs">Sector Expertise</text>
    <text class="navy" x="810" y="710" font-size="32" textLength="262" lengthAdjust="spacingAndGlyphs" transform="rotate(-90 810 710)">Wide Range of</text>
    <text class="navy" x="860" y="710" font-size="54" textLength="265" lengthAdjust="spacingAndGlyphs" transform="rotate(-90 860 710)">Industries</text>
    <text class="sky" x="877" y="480" font-size="44" textLength="238" lengthAdjust="spacingAndGlyphs">Hospitality</text>
    <text class="navy" x="877" y="545" font-size="68" textLength="240" lengthAdjust="spacingAndGlyphs">Sectors</text>
    <text class="navy" x="877" y="590" font-size="36" textLength="150" lengthAdjust="spacingAndGlyphs">Aviation</text>
    <text class="sky" x="1043" y="560" font-size="36" textLength="118" lengthAdjust="spacingAndGlyphs" transform="rotate(90 1043 560)">Office</text>
    <text class="navy" x="1088" y="560" font-size="28" textLength="152" lengthAdjust="spacingAndGlyphs" transform="rotate(90 1088 560)">Industrial</text>
    <text class="navy" x="899" y="670" font-size="22" textLength="63" lengthAdjust="spacingAndGlyphs" transform="rotate(-90 899 670)">Retail</text>
    <text class="navy" x="912" y="619" font-size="17" textLength="50" lengthAdjust="spacingAndGlyphs">Mixed</text>
    <text class="navy" x="912" y="643" font-size="26" textLength="50" lengthAdjust="spacingAndGlyphs">Use</text>
    <text class="sky" x="975" y="619" font-size="18" textLength="53" lengthAdjust="spacingAndGlyphs">Asset</text>
    <text class="sky" x="975" y="642" font-size="18" textLength="53" lengthAdjust="spacingAndGlyphs">Class</text>
    <text class="navy" x="910" y="672" font-size="21" textLength="118" lengthAdjust="spacingAndGlyphs">Residential</text>
    <text class="sky" x="877" y="710" font-size="36" textLength="198" lengthAdjust="spacingAndGlyphs">Healthcare</text>
  </g>
</svg>
</body>
</html>
```